A Referral Pad for a Specialist Surgeon to give to referring GPs

A referral pad allows general practitioners to easily refer patients to me by quickly filling in a form on a small pad that I provide them.

A two sided referral pad themed appropriately. Theming and designing the pad should be based on the general design/logo/imagery/colours etc. from my website www.marcuspellwright.com.au. I have a logo uploaded that should be used somewhere. I have also upload a headshot of myself which might or might not be used. Other choice of imagery and design features is up to the designer.

In terms of size of the pad I’m not quite sure what is best and will leave it up to the designers.

MORE DETAILED INFORMATION IS PROVIDED IN THE UPLOADED WORD FILE

Target Market(s)

General Practitioners referring to me

Industry/Entity Type

Healthcare

Contact Information for Business Card

A business card themed as per the referral pad design as as per general look and imagery found on www.marcuspellwright.com.au

Requirements
Must have
• Referral pad details found in uploaded Word document
Nice to have
Should not have

```html
<!DOCTYPE html>
<html lang="en">
<head>
<meta charset="utf-8">
<title>Marcus Pellwright – Referral Pad</title>
<link href="https://fonts.googleapis.com/css2?family=Cinzel:wght@400;600&family=Source+Sans+3:ital,wght@0,400;0,600;1,400&display=swap" rel="stylesheet">
<style>
:root{
  --teal:#1b7a72;
  --teal-light:#5fb4aa;
  --ink:#222;
  --rule:#555;
  --panel:#eef2f1;
  --box:#e7efee;
  --bg:#e9e6e1;
  --paper:#ffffff;
}
*{box-sizing:border-box;margin:0;padding:0}
html,body{width:1200px;height:1200px;overflow:hidden;background:var(--bg)}
body{position:relative;font-family:"Source Sans 3",sans-serif;color:var(--ink)}
.sheet{position:absolute;background:var(--paper);box-shadow:0 3px 10px rgba(0,0,0,.18);overflow:hidden}
.sheet--referral{left:18px;top:16px;width:562px;height:788px}
.sheet--details{left:624px;top:387px;width:562px;height:789px}
.abs{position:absolute;white-space:nowrap}
.brand{position:absolute;display:flex;align-items:center;gap:8px}
.brand__dot{width:40px;height:40px;border-radius:50%;background:var(--teal);flex:none}
.brand__name{font-family:"Cinzel",serif;font-weight:600;font-size:18px;color:var(--teal);letter-spacing:.2px;line-height:1;white-space:nowrap}
.brand__sub{font-family:"Cinzel",serif;font-size:7.5px;letter-spacing:1.1px;color:#777;margin-top:3px;white-space:nowrap}
.contact{font-size:12px;line-height:15px;display:flex;align-items:center;gap:4px}
.contact svg{width:12px;height:12px;fill:var(--teal)}
.banner{position:absolute;left:0;width:100%;background:var(--teal);color:#fff;font-family:"Cinzel",serif;text-align:center;letter-spacing:.6px}
.tag{position:absolute;left:0;width:180px;height:14px;background:var(--teal-light);color:#fff;font-family:"Cinzel",serif;font-size:10.5px;line-height:14px;padding-left:35px;letter-spacing:.4px}
.field{position:absolute;font-size:13px;display:flex;align-items:flex-end}
.field span{flex:1;border-bottom:1px solid var(--rule);margin-left:4px;height:13px}
.hint{color:#c9cfcf;font-size:10px;position:absolute;left:70px;bottom:1px}
.history-label{color:var(--teal);font-size:12px}
.history-box{position:absolute;left:27px;top:256px;width:508px;height:120px;background:var(--box);border-radius:4px}
.stamp{position:absolute;left:372px;top:394px;width:163px;height:124px;border:1px solid #666;border-radius:4px}
.stamp em{display:block;text-align:center;color:#d4d8d8;font-size:8.5px;font-style:normal;margin-top:1px}
.check{position:absolute;font-size:13px;display:flex;align-items:center;gap:6px}
.check i{width:12px;height:12px;border:1px solid #666;display:inline-block}
.check small{font-style:italic;font-size:8px}
.note{position:absolute;border:1px solid #444;border-radius:12px;font-style:italic;font-size:8.5px;line-height:12.5px}
.footer{position:absolute;left:0;bottom:0;width:100%;background:var(--teal);color:#fff;text-align:center;font-size:12px}
.link-head{position:absolute;left:32px;font-family:"Cinzel",serif;font-size:11.5px;color:var(--teal);text-decoration:underline;letter-spacing:.3px}
.copy{position:absolute;left:38px;font-size:13.5px;line-height:18px}
.criteria{position:absolute;left:38px;list-style:none;font-size:13.5px;line-height:17px}
.criteria li b{font-weight:400;display:inline-block;width:21px}
.panel{position:absolute;left:0;width:100%;background:var(--panel)}
.loc{position:absolute;font-size:12px;line-height:15.5px}
.loc b{font-weight:600}
.loc i{display:block}
.loc::before{content:"";position:absolute;left:-23px;top:5px;width:6px;height:6px;border-radius:50%;background:#222}
.loc--sm::before{left:-12px}
.col-head{position:absolute;color:var(--teal);font-weight:600;font-size:12.5px}
.photo{position:absolute;left:394px;top:550px;width:134px;height:162px;border:1px solid var(--teal);background:linear-gradient(180deg,#f4f4f3,#d9dcdc 60%,#3a3f47 100%)}
</style>
</head>
<body>

<section class="sheet sheet--referral">
  <div class="brand" style="left:26px;top:31px">
    <div class="brand__dot"></div>
    <div><div class="brand__name">MARCUS PELLWRIGHT</div><div class="brand__sub">GENERAL, UPPER GI &amp; BARIATRIC SURGEON</div></div>
  </div>
  <div class="abs contact" style="left:312px;top:27px"><svg viewBox="0 0 24 24"><path d="M6 2h4l2 5-3 2a11 11 0 0 0 6 6l2-3 5 2v4a2 2 0 0 1-2 2A18 18 0 0 1 4 4a2 2 0 0 1 2-2z"/></svg>(03) 9410 2286</div>
  <div class="abs contact" style="left:312px;top:46px"><svg viewBox="0 0 24 24"><path d="M6 2h12v6H6zM3 9h18v9h-3v4H6v-4H3zm5 6v5h8v-5z"/></svg>(03) 9410 2287</div>
  <div class="abs contact" style="left:312px;top:65px"><svg viewBox="0 0 24 24"><path d="M2 5h20v14H2zm2 2v.5l8 6 8-6V7z"/></svg>info@pellwrightsurgery.com.au</div>

  <div class="banner" style="top:86px;height:22px;font-size:15px;line-height:22px">PATIENT REFERRAL</div>

  <div class="tag" style="top:123px">PATIENT INFORMATION</div>
  <div class="abs" style="left:424px;top:136px;width:104px;border-bottom:1px solid var(--rule)"></div>
  <div class="field" style="left:34px;top:148px;width:494px">Name:<span></span></div>
  <div class="field" style="left:34px;top:169px;width:292px">DOB:<span style="margin-left:18px;position:relative"><em class="hint">DD/MMM/YYYY</em></span></div>
  <div class="field" style="left:312px;top:169px;width:216px">Gender:<span></span></div>
  <div class="field" style="left:34px;top:191px;width:210px">Phone:<span></span></div>
  <div class="field" style="left:234px;top:191px;width:294px">e-mail:<span style="margin-left:1px"></span></div>
  <div class="field" style="left:34px;top:213px;width:494px">Address:<span style="margin-left:0"></span></div>
  <div class="abs history-label" style="left:35px;top:238px">Medical history</div>
  <div class="history-box"></div>

  <div class="tag" style="top:394px">REFERRING DOCTOR</div>
  <div class="field" style="left:35px;top:418px;width:324px">Name:<span style="margin-left:8px"></span></div>
  <div class="field" style="left:35px;top:439px;width:324px">Phone:<span style="margin-left:5px"></span></div>
  <div class="field" style="left:35px;top:459px;width:324px">Provider Number:<span style="margin-left:3px"></span></div>
  <div class="field" style="left:35px;top:480px;width:324px">Clinic Address:<span style="margin-left:3px"></span></div>
  <div class="abs" style="left:37px;top:514px;width:322px;border-bottom:1px solid var(--rule)"></div>
  <div class="stamp"><em>Seal/ Stamp</em></div>

  <div class="tag" style="top:527px">PROCEDURE CHOICE</div>
  <div class="check" style="left:35px;top:551px"><i></i>Bariatric Surgery <small>(details &amp; eligibility overleaf)</small></div>
  <div class="field" style="left:75px;top:572px;width:289px">a. Patient Weight (Kgs):<span style="margin-left:2px"></span></div>
  <div class="abs" style="left:75px;top:590px;font-size:13px">b. Patient BMI:</div>
  <div class="abs" style="left:213px;top:602px;width:151px;border-bottom:1px solid var(--rule)"></div>
  <div class="abs" style="left:75px;top:609px;font-size:13px">c. Diabetic?</div>
  <div class="check" style="left:213px;top:610px"><i></i>Yes</div>
  <div class="check" style="left:266px;top:610px"><i></i>No</div>
  <div class="check" style="left:35px;top:628px"><i></i>Abdominoplasty or Arm Reduction after weight loss</div>
  <div class="check" style="left:35px;top:649px"><i></i>Antireflux/Hiatus Hernia Surgery</div>
  <div class="check" style="left:35px;top:670px"><i></i>Gallbladder</div>
  <div class="check" style="left:35px;top:690px"><i></i>Hernia</div>
  <div class="check" style="left:35px;top:710px"><i></i>Endoscopy</div>
  <div class="check" style="left:35px;top:731px"><i></i>Other general surgery*</div>
  <div class="note" style="left:376px;top:690px;width:159px;height:54px;padding:7px 8px">*Includes skin, lumps &amp; bumps, peri-anal/haemorrhoids, varicose veins, carpal tunnel.</div>

  <div class="footer" style="height:31px;line-height:29px">www.marcuspellwright.com.au</div>
</section>

<section class="sheet sheet--details">
  <div class="brand" style="left:30px;top:27px">
    <div class="brand__dot" style="width:50px;height:50px"></div>
    <div><div class="brand__name" style="font-size:21px">MARCUS PELLWRIGHT</div><div class="brand__sub">GENERAL, UPPER GI &amp; BARIATRIC SURGEON</div></div>
  </div>
  <div class="banner" style="top:87px;height:21px;font-size:12.5px;line-height:21px">BARIATRIC SURGERY DETAILS &amp; ELIGIBILITY</div>

  <div class="link-head" style="top:124px">BARIATRIC SURGERY PROCEDURES OFFERED</div>
  <p class="copy" style="top:142px">Sleeve Gastrectomy, Gastric Bypass, Gastric Banding, Revisional surgery,<br>Endobarrier or Intra gastric balloon implantation, Gastric Band management.<br>Abdominoplasty or Arm Reduction for weight loss patients.</p>

  <div class="link-head" style="top:214px">STANDARD ELIGIBILITY CRITERIA FOR BARIATRIC SURGERY</div>
  <ol class="criteria" style="top:240px">
    <li><b>1.</b>BMI &gt; 40</li>
    <li><b>2.</b>BMI &gt; 35 with diabetes or other obesity related co-morbidity</li>
    <li><b>3.</b>BMI 30 – 35 selected cases</li>
  </ol>
  <div class="note" style="left:32px;top:310px;width:499px;height:43px;padding:5px 7px;font-size:11.5px;line-height:16px;border-radius:4px">Please note that for sleeve gastrectomy &amp; gastric bypass procedures private health insurance of the appropriate level is mandatory to proceed with surgery.</div>

  <div class="banner" style="top:377px;height:18px;font-size:12.5px;line-height:18px">OPERATING LOCATIONS</div>
  <div class="panel" style="top:395px;height:113px"></div>
  <div class="loc" style="left:67px;top:416px"><b>Yarrawood Richmond Hospital</b><i>42 Kelvin Rd, Richmond</i></div>
  <div class="loc" style="left:67px;top:462px"><b>Yarrawood Eastern Hospital</b><i>Suite 14, Level 3, 7 Halden Street, Box Hill</i></div>
  <div class="loc loc--sm" style="left:341px;top:416px"><b>Whitehorse Public Hospital</b><i>12 Halden St, Box Hill</i></div>
  <div class="loc loc--sm" style="left:341px;top:462px"><b>Coastal Ranges Hospital</b><i>51-55 Marlow Rd, Foster</i></div>

  <div class="banner" style="top:508px;height:21px;font-size:12.5px;line-height:21px">CONSULTING LOCATIONS</div>
  <div class="panel" style="top:529px;height:226px"></div>
  <div class="col-head" style="left:39px;top:538px">Regional</div>
  <div class="col-head" style="left:228px;top:538px">Melbourne</div>
  <div class="loc loc--sm" style="left:53px;top:562px"><b>Goldfields Primary Care Clinic</b><i>210-212 Garrick Street,<br>Bendigo</i></div>
  <div class="loc loc--sm" style="left:53px;top:617px"><b>Campaspe Specialist Centre</b><i>38 Farrell Street, Kyneton</i></div>
  <div class="loc loc--sm" style="left:53px;top:656px"><b>Prom Coast Medical Centre</b><i>19 Marlow Rd, Foster</i></div>
  <div class="loc loc--sm" style="left:53px;top:695px"><b>Latrobe Valley Medical Group</b><i>3-5 Tanner St, Moe</i></div>
  <div class="loc loc--sm" style="left:240px;top:562px"><b>CBD</b> <i style="display:inline">Level 7, 118 Exhibition</i><i>Street, Melbourne</i></div>
  <div class="loc loc--sm" style="left:240px;top:601px"><b>Yarrawood Eastern</b><i>Suite 14, Level 3, 7 Halden</i><i>Street, Box Hill</i></div>
  <div class="loc loc--sm" style="left:240px;top:654px"><b>Vitality on Ferntree</b><i>2/640 Ferntree Road,</i><i>Rowville</i></div>
  <div class="photo" role="img" aria-label="Headshot of the surgeon"></div>

  <div class="footer" style="height:34px"></div>
</section>

</body>
</html>
```